Design some Business Cards for PeachwoodCreative

Hi

I'm looking for a business card design for [url removed, login to view]

Please include the web address on the business card. I'm looking for something creative. I can do the generic designs on my own.

Attached please find the logo.

Name : Maribel Okafor
Phone : 1-272 614 8820
Email : maribel@[url removed, login to view]
Address : Philadelphia, PA 19387

```html
<!DOCTYPE html>
<html lang="en">
<head>
<meta charset="utf-8">
<title>PeachwoodCreative Business Cards</title>
<link rel="stylesheet" href="https://fonts.googleapis.com/css2?family=Crimson+Text:wght@400;600&family=Arimo:wght@400&display=swap">
<style>
  :root {
    --page: #ece9e4;
    --orange: #e8470f;
    --orange-deep: #c93a08;
    --orange-light: #f4622a;
    --black: #111111;
    --white: #ffffff;
    --ink: #2b2b2b;
    --serif: "Crimson Text", Georgia, serif;
    --sans: "Arimo", Arial, sans-serif;
  }
  html, body {
    margin: 0;
    padding: 0;
    width: 1200px;
    height: 900px;
    overflow: hidden;
    background: var(--page);
  }
  .sheet {
    position: relative;
    width: 1200px;
    height: 900px;
  }
  .card {
    position: absolute;
    left: 250px;
    width: 700px;
    height: 400px;
    overflow: hidden;
    box-shadow: 0 6px 18px rgba(0,0,0,0.18);
    background: var(--white);
  }
  .card--front { top: 30px; }
  .card--back { top: 470px; }
  .card-art {
    position: absolute;
    inset: 0;
    width: 700px;
    height: 400px;
  }
  .front-identity {
    position: absolute;
    left: 410px;
    top: 130px;
  }
  .front-name {
    font-family: var(--serif);
    font-size: 36px;
    color: var(--white);
    margin: 0;
    line-height: 1;
  }
  .front-company {
    font-family: var(--serif);
    font-size: 24px;
    color: var(--ink);
    margin: 6px 0 0;
    line-height: 1;
  }
  .brand {
    position: absolute;
    left: 80px;
    top: 48px;
  }
  .brand-mark {
    width: 56px;
    height: 56px;
    background: var(--orange);
    margin-bottom: 14px;
  }
  .brand-name {
    font-family: var(--serif);
    font-size: 30px;
    font-weight: 600;
    color: var(--ink);
    margin: 0;
    line-height: 1;
  }
  .brand-web {
    font-family: var(--serif);
    font-size: 17px;
    color: var(--ink);
    margin: 6px 0 0;
  }
  .holder {
    position: absolute;
    left: 56px;
    top: 228px;
  }
  .holder-name {
    font-family: var(--serif);
    font-size: 32px;
    color: var(--orange-light);
    margin: 0;
    line-height: 1;
  }
  .holder-role {
    font-family: var(--serif);
    font-size: 20px;
    color: var(--white);
    margin: 2px 0 0;
    line-height: 1;
  }
  .contact-list {
    position: absolute;
    left: 56px;
    top: 306px;
    margin: 0;
    padding: 0;
    list-style: none;
  }
  .contact-item {
    display: flex;
    align-items: center;
    gap: 12px;
    font-family: var(--sans);
    font-size: 15px;
    color: var(--white);
    height: 28px;
  }
  .contact-icon {
    width: 16px;
    height: 16px;
    flex: none;
  }
</style>
</head>
<body>
<main class="sheet">

  <section class="card card--front" aria-label="Card front">
    <svg class="card-art" viewBox="0 0 700 400" aria-hidden="true">
      <defs>
        <linearGradient id="frontFill" x1="0" y1="0" x2="1" y2="1">
          <stop offset="0" stop-color="#f0561a"/>
          <stop offset="1" stop-color="#c93a08"/>
        </linearGradient>
      </defs>
      <rect width="700" height="400" fill="url(#frontFill)"/>
      <path d="M0 0 H700 V34 H330 Q310 34 296 52 L272 84 Q262 96 244 96 H0 Z" fill="#111111"/>
      <circle cx="210" cy="240" r="92" fill="#ffffff"/>
    </svg>
    <div class="front-identity">
      <p class="front-name">Maribel Okafor</p>
      <p class="front-company">Peachwood creative</p>
    </div>
  </section>

  <section class="card card--back" aria-label="Card back">
    <svg class="card-art" viewBox="0 0 700 400" aria-hidden="true">
      <defs>
        <linearGradient id="backFill" x1="0" y1="0" x2="1" y2="1">
          <stop offset="0" stop-color="#c93a08"/>
          <stop offset="1" stop-color="#f0561a"/>
        </linearGradient>
      </defs>
      <rect width="700" height="400" fill="#ffffff"/>
      <path d="M0 222 H336 Q352 222 364 210 L404 170 Q414 160 430 156 L700 92 V400 H0 Z" fill="#111111"/>
      <path d="M0 292 H350 Q366 292 378 280 L420 232 Q430 222 446 218 L700 150 V400 H0 Z" fill="url(#backFill)"/>
    </svg>

    <div class="brand">
      <div class="brand-mark"></div>
      <p class="brand-name">Peachwood creative</p>
      <p class="brand-web">www.peachwoodcreative.com</p>
    </div>

    <div class="holder">
      <p class="holder-name">Maribel Okafor</p>
      <p class="holder-role">Admine</p>
    </div>

    <ul class="contact-list">
      <li class="contact-item">
        <svg class="contact-icon" viewBox="0 0 16 16" aria-hidden="true"><path d="M8 1 L15 8 H12.5 V15 H9.5 V10.5 H6.5 V15 H3.5 V8 H1 Z" fill="#111111"/></svg>
        Philadelphia, PA 19387
      </li>
      <li class="contact-item">
        <svg class="contact-icon" viewBox="0 0 16 16" aria-hidden="true"><rect x="1" y="3" width="14" height="10" fill="#111111"/><path d="M1 3 L8 9 L15 3" stroke="#e8470f" stroke-width="1.2" fill="none"/></svg>
        Email: maribel@peachwoodcreative.com
      </li>
      <li class="contact-item">
        <svg class="contact-icon" viewBox="0 0 16 16" aria-hidden="true"><path d="M2 5 Q8 0 14 5 L12 7 L10 5.5 H6 L4 7 Z" fill="#111111"/><rect x="3" y="8" width="10" height="6" rx="1" fill="#111111"/></svg>
        Ph: 1-272 614 8820
      </li>
    </ul>
  </section>

</main>
</body>
</html>
```